hi all

Im after a new age looking business card with my company logo on it

must include these details, I would like the PH and Email to be symbols

If the colours used for card could be kept within the colours used in logo that I have supplied that would be great, if another colour is to be used dark grey would be ok. no light bulbs etc thanks

Details below to be incorporated on card

Damian Holloway

Lic E871302

PH 0219647381

E info@brightvaleelectrical.example.nz

Domestic Commercial Industrial Electricians

```html
<!DOCTYPE html>
<html lang="en">
<head>
<meta charset="utf-8">
<title>Brightvale Electrical – Business Card</title>
<link rel="stylesheet" href="https://fonts.googleapis.com/css2?family=Arimo:wght@400;700&display=swap">
<style>
  :root{
    --brand-blue:#0f7fcb;
    --ink:#111111;
    --text-grey:#444444;
    --paper:#ffffff;
    --backdrop:#b9b9b9;
  }
  *{box-sizing:border-box;margin:0;padding:0}
  html,body{width:1200px;height:900px;overflow:hidden}
  body{background:var(--backdrop);font-family:"Arimo",Arial,sans-serif;position:relative}

  .card{position:absolute;width:560px;height:320px;border-radius:34px;overflow:hidden}
  .card--back{left:80px;top:90px;background:var(--brand-blue);color:var(--paper)}
  .card--front{left:560px;top:490px;background:var(--paper)}

  .brand{display:flex;align-items:center;gap:12px}
  .brand__dot{width:38px;height:38px;border-radius:50%;flex:none}
  .brand__name{font-weight:700;line-height:1;letter-spacing:1px}
  .brand__name small{display:block;font-size:.42em;letter-spacing:5px;margin-top:6px;text-align:right}

  .card--back .brand{position:absolute;left:0;right:0;top:96px;justify-content:center}
  .card--back .brand__dot{background:var(--paper)}
  .card--back .brand__name{font-size:46px;color:var(--paper)}
  .card--back .tagline{position:absolute;left:0;right:0;bottom:46px;text-align:center;font-size:15px;letter-spacing:.3px}

  .card--front .brand{position:absolute;right:34px;top:38px}
  .card--front .brand__dot{background:var(--brand-blue);width:30px;height:30px}
  .card--front .brand__name{font-size:34px;color:var(--brand-blue)}

  .swoosh{position:absolute;inset:0}

  .holder{position:absolute;left:40px;top:184px;width:440px}
  .holder__row{display:flex;align-items:center;gap:12px}
  .holder__name{font-size:22px;font-weight:700;color:var(--brand-blue);letter-spacing:.5px;white-space:nowrap}
  .holder__rule{flex:1;height:1.5px;background:var(--brand-blue);margin-top:4px}
  .holder__licence{font-size:14px;color:var(--text-grey);margin-top:4px}

  .contacts{list-style:none;margin-top:14px}
  .contacts li{display:flex;align-items:center;gap:8px;font-size:13px;color:var(--text-grey);margin-bottom:4px;white-space:nowrap}
  .contacts svg{width:12px;height:12px;fill:var(--brand-blue);flex:none}
  .contacts .accent{color:var(--brand-blue)}
</style>
</head>
<body>

<section class="card card--back">
  <div class="brand">
    <span class="brand__dot"></span>
    <span class="brand__name">BRIGHTVALE<small>ELECTRICAL</small></span>
  </div>
  <p class="tagline">Domestic Commercial Industrial Electricians</p>
</section>

<section class="card card--front">
  <svg class="swoosh" viewBox="0 0 560 320" aria-hidden="true">
    <path d="M300 320 C365 248 450 190 548 158 C458 196 378 254 320 320 Z" fill="var(--ink)"/>
    <path d="M330 320 C392 256 470 204 560 176 L560 320 Z" fill="var(--brand-blue)"/>
  </svg>

  <div class="brand">
    <span class="brand__dot"></span>
    <span class="brand__name">BRIGHTVALE<small>ELECTRICAL</small></span>
  </div>

  <div class="holder">
    <div class="holder__row">
      <h1 class="holder__name">DAMIAN HOLLOWAY</h1>
      <span class="holder__rule"></span>
    </div>
    <p class="holder__licence">Lic E871302</p>
    <ul class="contacts">
      <li><svg viewBox="0 0 24 24"><path d="M6.6 10.8a15 15 0 0 0 6.6 6.6l2.2-2.2a1 1 0 0 1 1-.25 11.4 11.4 0 0 0 3.6.57 1 1 0 0 1 1 1V20a1 1 0 0 1-1 1A17 17 0 0 1 3 4a1 1 0 0 1 1-1h3.5a1 1 0 0 1 1 1c0 1.25.2 2.45.57 3.57a1 1 0 0 1-.25 1z"/></svg><span>0219647381</span></li>
      <li><svg viewBox="0 0 24 24"><path d="M2 5h20v14H2z M2 5l10 8 10-8" stroke="#fff" stroke-width="1.5"/></svg><span>info@brightvaleelectrical.example.nz</span></li>
      <li><svg viewBox="0 0 24 24"><circle cx="12" cy="12" r="10"/></svg><span>www.<span class="accent">brightvaleelectrical</span>.example.nz</span></li>
    </ul>
  </div>
</section>

</body>
</html>
```